Teodor Ravik, MD Print Package_Trifold

Need a trifold brochure designed. The business is a cosmetic surgery office with cosmetic procedures involving face surgery, body surgery, breast surgery, and skin care treatments. At this point, we would like to see a brochure with some more white space.

A little bit about the doctor for character reference:
Dr. Teodor Ravik believes the art of cosmetic surgery is in listening to his patients. He builds each treatment plan on a solid foundation of communication between doctor and patient and spends a considerable amount of time getting to know the people he treats — taking their goals into account and offering the best options to meet those goals. At our state-of-the-art Bayfield Aesthetic Institute, you are not just a patient; You are our guest.

Their website for further information and for color scheme reference, as the client would like the brochure to match his website (ie: ocean blue/teal, grays and black), is http://www.drtravensolo.example/

Attached is a brochure that the client created a few months back. This shows a general idea of how he would like the layout to be and the information to put on the trifold.

Also Attached are two additional Before & Afters for the brochure, per the client's request. As well as a picture of the Vexa Beam machine that performs these procedures.

Also attached is a brochure intake document for further guidelines as well.
Updates

Industry/Entity Type

Business

Requirements
Must have
• If utilizing any staff photos - please be sure to use Dr. Teodor Ravik, you can find him here:
• http://www.drtravensolo.example/about

```html
<!DOCTYPE html>
<html lang="en">
<head>
<meta charset="utf-8">
<title>Teodor Ravik, MD – Trifold Brochure</title>
<link href="https://fonts.googleapis.com/css2?family=Lato:wght@400;700&family=PT+Serif:wght@400;700&display=swap" rel="stylesheet">
<style>
  :root {
    --page: #e6e9eb;
    --cream: #fbf6e2;
    --slate: #476877;
    --slate-dark: #3b5a69;
    --teal-light: #5f8696;
    --heading-teal: #2c7f98;
    --cyan: #8fe6f0;
    --pill: #b6f1f6;
    --ink: #4a4a4a;
    --white: #ffffff;
  }
  * { box-sizing: border-box; margin: 0; padding: 0; }
  html, body { width: 1200px; height: 899px; overflow: hidden; }
  body { background: var(--page); font-family: "Lato", sans-serif; position: relative; }

  .brochure {
    position: absolute; left: 60px; top: 31px;
    width: 1080px; height: 836px;
    background: var(--cream);
    box-shadow: 0 6px 24px rgba(0,0,0,.25);
    overflow: hidden;
  }
  .brochure__shapes { position: absolute; inset: 0; }

  .serif-heading {
    font-family: "PT Serif", serif; font-weight: 700;
    font-size: 18px; letter-spacing: .3px; text-transform: uppercase;
  }

  /* Left panel */
  .fees { position: absolute; left: 33px; top: 26px; width: 320px; }
  .fees .serif-heading { color: var(--heading-teal); padding-left: 4px; margin-bottom: 6px; }
  .fees p { font-size: 12.4px; line-height: 1.25; color: var(--ink); text-align: justify; }
  .loan-list { list-style: none; margin-top: 18px; padding-left: 20px; width: 200px; }
  .loan-list li { position: relative; font-size: 12.4px; color: var(--ink); line-height: 1.25; margin-bottom: 8px; }
  .loan-list li::before {
    content: ""; position: absolute; left: -16px; top: 5px;
    width: 6px; height: 6px; border-radius: 50%; background: var(--heading-teal);
  }

  /* Middle panel */
  .about { position: absolute; left: 383px; top: 26px; width: 320px; color: var(--white); }
  .about .serif-heading { color: var(--white); margin-bottom: 6px; }
  .about p { font-size: 12.4px; line-height: 1.25; }

  .services { position: absolute; left: 33px; top: 630px; width: 360px; color: var(--white); }
  .services__title {
    display: inline-block; margin-left: 62px;
    background: var(--pill); color: var(--heading-teal);
    font-family: "PT Serif", serif; font-weight: 700; font-size: 17px;
    padding: 3px 18px; border-radius: 14px;
  }
  .services__intro { font-weight: 700; font-size: 13.6px; line-height: 1.3; margin-top: 22px; width: 330px; }
  .services__list {
    list-style: none; display: grid; grid-template-columns: 150px 160px;
    row-gap: 10px; margin-top: 18px; padding-left: 14px;
  }
  .services__list li { position: relative; font-weight: 700; font-size: 13.4px; }
  .services__list li::before {
    content: ""; position: absolute; left: -13px; top: 6px;
    width: 6px; height: 6px; border-radius: 50%; background: var(--white);
  }

  .call { position: absolute; left: 420px; top: 735px; width: 280px; }
  .call__label { font-size: 23px; font-weight: 700; color: var(--white); letter-spacing: .2px; }
  .call__number { font-size: 30px; font-weight: 700; color: var(--cyan); margin-top: 2px; }

  /* Right panel */
  .web-pill {
    position: absolute; left: 768px; top: 30px; width: 222px; height: 28px;
    background: var(--cream); border-radius: 14px;
    color: var(--slate-dark); font-family: "PT Serif", serif; font-weight: 700;
    font-size: 15px; text-align: center; line-height: 28px;
  }
  .brand { position: absolute; left: 770px; top: 92px; display: flex; align-items: center; gap: 12px; }
  .brand__dot { width: 22px; height: 22px; border-radius: 50%; background: var(--white); }
  .brand__name { color: var(--white); font-size: 17px; font-weight: 400; line-height: 1.25; }

  .tagline { position: absolute; left: 720px; top: 706px; width: 360px; text-align: center; color: var(--white); }
  .tagline__small { font-size: 19px; font-weight: 700; line-height: 1.3; }
  .tagline__big {
    font-family: "PT Serif", serif; color: var(--cyan); font-size: 28px;
    line-height: 1.05; margin-top: 2px;
  }
  .tagline__options { font-family: "PT Serif", serif; color: var(--cyan); font-size: 20px; }
</style>
</head>
<body>
<main class="brochure">
  <svg class="brochure__shapes" width="1080" height="836" viewBox="0 0 1080 836">
    <defs>
      <linearGradient id="panelSlate" x1="0" y1="0" x2="0" y2="1">
        <stop offset="0" stop-color="#527585"/>
        <stop offset="1" stop-color="#3e5f6e"/>
      </linearGradient>
      <linearGradient id="beach" x1="0" y1="0" x2="0" y2="1">
        <stop offset="0" stop-color="#9fd3ec"/>
        <stop offset=".45" stop-color="#d8b59c"/>
        <stop offset=".8" stop-color="#3f7fc4"/>
        <stop offset="1" stop-color="#2d5fa8"/>
      </linearGradient>
      <radialGradient id="portraitTone" cx=".5" cy=".45" r=".6">
        <stop offset="0" stop-color="#c99a7e"/>
        <stop offset=".6" stop-color="#8c7d86"/>
        <stop offset="1" stop-color="#5a6fa0"/>
      </radialGradient>
      <radialGradient id="skinTone" cx=".5" cy=".5" r=".6">
        <stop offset="0" stop-color="#f1dccf"/>
        <stop offset="1" stop-color="#d4b2a0"/>
      </radialGradient>
    </defs>

    <!-- middle panel top block -->
    <path d="M367,0 H720 V300 C640,330 560,300 480,330 C430,348 395,345 367,340 Z" fill="var(--slate)"/>

    <!-- lower wave band -->
    <path d="M0,585 C110,520 220,500 340,525 C460,550 570,600 720,660 V836 H0 Z" fill="var(--teal-light)"/>
    <path d="M0,610 C120,555 230,540 350,560 C470,585 580,635 720,690 V836 H0 Z" fill="var(--slate-dark)"/>
    <path d="M0,585 C110,520 220,500 340,525 C460,550 570,600 720,660" fill="none" stroke="var(--cream)" stroke-width="3"/>
    <rect x="0" y="818" width="720" height="18" fill="var(--white)"/>

    <!-- right panel -->
    <rect x="720" y="0" width="360" height="836" fill="url(#panelSlate)"/>
    <g role="img" aria-label="Beach photo of a woman's torso in a white bikini with a blue wrap">
      <path d="M720,215 C820,190 960,170 1080,175 V672 C960,700 830,695 720,675 Z" fill="url(#beach)" stroke="var(--cream)" stroke-width="7"/>
    </g>

    <!-- circular photos -->
    <g role="img" aria-label="Portrait of Dr. Teodor Ravik">
      <circle cx="548" cy="350" r="96" fill="url(#portraitTone)" stroke="var(--cream)" stroke-width="3"/>
      <circle cx="548" cy="350" r="88" fill="none" stroke="var(--slate-dark)" stroke-width="5"/>
    </g>
    <g role="img" aria-label="Photo of a woman relaxing during a skin care treatment">
      <circle cx="268" cy="510" r="86" fill="url(#skinTone)" stroke="var(--slate-dark)" stroke-width="6"/>
    </g>
    <g role="img" aria-label="Photo of a woman in lingerie for breast surgery">
      <circle cx="453" cy="555" r="68" fill="#b9a59a" stroke="var(--slate-dark)" stroke-width="6"/>
    </g>
    <g role="img" aria-label="Photo of a woman with smooth facial skin">
      <circle cx="624" cy="616" r="68" fill="url(#skinTone)" stroke="var(--slate-dark)" stroke-width="6"/>
    </g>
  </svg>

  <section class="fees">
    <h2 class="serif-heading">Fees and Insurance</h2>
    <p>Costs of plastic surgery depend on the type of procedure received and the complexity of the operation, among other factors. Fees are usually paid prior to surgery. Most cosmetic plastic surgery procedures are considered elective surgeries and are therefore generally not covered under insurance plans. However, there are exceptions. Some operations, such as breast reduction and breast reconstruction, may be covered by insurance. Check with Dr. Ravik to find out if your procedure could be covered by insurance.</p>
    <ul class="loan-list">
      <li>Immediate decisions for loans under $35,000</li>
      <li>Term options out to 84 months (affordable monthly payments)</li>
      <li>No collateral required</li>
      <li>No prepayment penalties</li>
      <li>Fast &amp; easy loan inquiry process</li>
      <li>100% Confidential</li>
    </ul>
  </section>

  <section class="about">
    <h2 class="serif-heading">About Dr. Teodor Ravik</h2>
    <p>Dr. Teodor Ravik believes the art of cosmetic surgery is in listening to his patients. He builds each treatment plan on a solid foundation of communication between doctor and patient and spends a considerable amount of time getting to know the people he treats — taking their goals into account and offering the best options to meet those goals. At our state-of-the-art Bayfield Aesthetic Institute, you are not just a patient; You are our guest.</p>
  </section>

  <section class="services">
    <h2 class="services__title">OUR SERVICES</h2>
    <p class="services__intro">We offer a variety of cosmetic procedures which include:</p>
    <ul class="services__list">
      <li>Face Surgery</li>
      <li>Breast Surgery</li>
      <li>Body Surgery</li>
      <li>Skin Care Treatments</li>
    </ul>
  </section>

  <div class="call">
    <div class="call__label">CALL US ANY TIME</div>
    <div class="call__number">(302) 555-0148</div>
  </div>

  <div class="web-pill">www.drtravensolo.example</div>
  <div class="brand">
    <span class="brand__dot"></span>
    <span class="brand__name">Bayfield Aesthetic Institute<br>Teodor Ravik, MD</span>
  </div>

  <div class="tagline">
    <div class="tagline__small">OFFERING A<br>COMPREHENSIVE RANGE OF</div>
    <div class="tagline__big">COSMETIC SURGERY</div>
    <div class="tagline__options">OPTIONS</div>
  </div>
</main>
</body>
</html>
```